KRV Holdfast Manufacturer New Web Design

We need a new theme designed for metal fastener manufacturing company, KRV Holdfast Group, a $60M division of Benmore Forge Holdings, Inc. We manufacture screw, pins and washers to industrial customers (non-Automotive) such as Tallow Appliance, Marcus Fenwold, BRU, Veltrin, etc. Our current website is www.holdfastparts.example. We would like to stick with the same logo/color scheme, however, I'm aiming to modernize the website's look and feel.

Here are some of our competitor's websites:
- https://www.torvanix.example/
- http://quellbrook.example/
- http://www.morrowbuiltcouplingworks.example/
- http://pegsandoddments.example/
- http://www.dunmerebolting.example/

Target Market(s)

We primarily want to target engineers working in the following markets:
- Appliance (Tallow Appliance, Kelvanor)
- Ag (Fenwold, BRU)
- Recreational Vehicle (Veltrin, Briar Fox)
- Outdoor Power (Oldmeadow, Vexa)

We secondarily want to target buyers working at the above markets as well as buyers at Fastener distributors such as Boltrin, Provision Dynamics, Hollis Parfet.

Industry/Entity Type

Metal Forging

Number of Pages Required

1 page

Requirements
Must have
• For products: "Threaded" product as the primary focus. "Pins" product is the secondary focus, followed by all others.
• Please use same logo and color scheme as I do not plan to change.
Nice to have
• Highlight our featured proprietary products (pamphlets attached). KRV Holdfast's KIN-V, LumDrive, Holdfast Spiral, Pelmont.

```html
<!DOCTYPE html>
<html lang="en">
<head>
<meta charset="utf-8">
<title>KRV Holdfast Group</title>
<link rel="stylesheet" href="https://fonts.googleapis.com/css2?family=Roboto:wght@400;500;700;900&display=swap">
<style>
:root{
  --blue:#00b4e0;
  --teal:#22c7a4;
  --ink:#2a2a2a;
  --text:#555;
  --muted:#8a8a8a;
  --light:#efefef;
  --footer:#1f1f1f;
  --footer-text:#b9b9b9;
  --white:#fff;
}
*{box-sizing:border-box;margin:0;padding:0}
html,body{width:1200px;height:2594px;overflow:hidden}
body{font-family:"Roboto",Arial,sans-serif;color:var(--text);background:var(--white);position:relative}
.abs{position:absolute}

/* header + hero */
.hero{left:0;top:0;width:1200px;height:612px;border-top:3px solid var(--blue);
  background:linear-gradient(180deg,#f2f4f5 0%,#d8dde0 45%,#a9b1b6 100%)}
.hero-photo{left:0;top:150px;width:1200px;height:462px;
  background:radial-gradient(ellipse at 45% 70%,#8f9aa1 0%,#b8c0c5 45%,rgba(220,224,226,0) 80%)}
.brand{left:147px;top:16px;display:flex;align-items:center;gap:10px}
.brand-dot{width:46px;height:46px;border-radius:50%;background:var(--blue)}
.brand-name{font-size:22px;font-weight:700;color:var(--blue)}
.nav{right:145px;top:36px;display:flex;gap:21px;list-style:none}
.nav li{font-size:11.5px;font-weight:500;color:#333;text-transform:uppercase}
.tagline{left:700px;top:138px;width:355px;text-align:right;font-weight:700;line-height:1.05;text-transform:uppercase}
.tagline span{display:block}
.tagline .l1{font-size:27px;color:#333}
.tagline .l2{font-size:27px;color:#333;font-weight:400}
.tagline .l3{font-size:27px;color:var(--blue)}

/* welcome */
.welcome-title{left:147px;top:666px;border-left:4px solid var(--blue);padding-left:14px;font-size:23px;font-weight:700;color:var(--ink);text-transform:uppercase;line-height:32px}
.welcome-title em{font-style:normal;color:var(--blue)}
.welcome-title i{font-style:normal;color:#8b8b8b}
.welcome-lead{left:166px;top:701px;width:380px;font-size:10.5px;font-weight:500;color:#444;text-transform:uppercase;line-height:15px}
.welcome-body{left:166px;top:734px;width:412px;font-size:10.5px;line-height:15.5px;color:#666}
.feature-line{left:187px;top:850px;width:2px;height:170px;background:var(--teal)}
.feature{left:162px;width:420px;display:flex;gap:18px}
.feature-icon{width:52px;height:52px;border-radius:50%;background:var(--teal);border:4px solid #c7f0e6;flex:none;display:flex;align-items:center;justify-content:center}
.feature h3{font-size:15px;font-weight:500;color:#333;margin:4px 0 5px}
.feature p{font-size:10.5px;line-height:15px;color:#777;width:340px}
.welcome-photo{left:628px;top:674px;width:425px;height:356px;background:linear-gradient(135deg,#5c6f86 0%,#8ea2b4 45%,#d67a3a 75%,#34475c 100%)}

/* services */
.services{left:0;top:1094px;width:1200px;height:343px;background:linear-gradient(90deg,#ececec,#e3e3e3)}
.services-kicker{left:147px;top:1143px;font-size:21px;font-weight:700;color:var(--ink);text-transform:uppercase}
.services-title{left:147px;top:1164px;font-size:41px;font-weight:700;color:var(--ink);text-transform:uppercase;letter-spacing:-1px}
.services-rule{left:147px;top:1216px;width:335px;height:1px;background:#bbb}
.services-text{left:147px;width:335px;font-size:10.5px;line-height:15px;color:#333;font-weight:500}
.btn-dark{background:#2b2b2b;color:var(--white);font-size:11px;font-weight:700;text-transform:uppercase;display:flex;align-items:center;justify-content:center;gap:8px}
.service-tile{width:234px;height:132px}
.service-photo{width:100%;height:106px}
.service-label{height:26px;background:var(--teal);color:var(--white);font-size:14px;font-weight:700;text-transform:uppercase;text-align:center;line-height:26px}

/* quote band */
.quote{left:0;top:1437px;width:1200px;height:192px;background:var(--blue)}
.field{height:33px;background:#eafaff;border:1px solid #cfeef7;font-size:9.5px;color:#777;padding:0 12px;line-height:31px}
.quote-mark{left:998px;top:1472px}
.quote-kicker{left:800px;top:1530px;width:254px;text-align:right;font-size:13px;font-weight:700;color:var(--white);text-transform:uppercase}
.quote-title{left:700px;top:1540px;width:355px;text-align:right;font-size:34px;font-weight:700;color:var(--white);text-transform:uppercase;letter-spacing:-1px}

/* news */
.news-title{left:0;top:1668px;width:1200px;text-align:center;font-size:35px;font-weight:700;color:var(--ink);text-transform:uppercase;letter-spacing:-.5px}
.news-rule{left:572px;top:1722px;width:57px;height:4px;background:var(--blue)}
.news-card{width:427px;height:172px;background:var(--light);display:flex}
.news-card.is-active{background:var(--teal)}
.news-photo{width:180px;height:172px;flex:none;position:relative}
.news-date{position:absolute;left:8px;top:0;width:30px;height:32px;background:var(--teal);color:var(--white);text-align:center;font-weight:700;line-height:1}
.news-date b{display:block;font-size:13px;padding-top:4px}
.news-date small{font-size:7px}
.news-body{padding:25px 18px 0 18px}
.news-body h4{font-size:13px;font-weight:700;color:#333;text-transform:uppercase;margin-bottom:7px}
.news-meta{font-size:9.5px;color:#555;display:flex;gap:16px;margin-bottom:12px}
.news-body p{font-size:10.5px;line-height:15px;color:#444}
.is-active h4,.is-active .news-meta,.is-active p{color:var(--white)}

/* footer */
.footer{left:0;top:2206px;width:1200px;height:339px;background:var(--footer)}
.stat{top:2240px;color:var(--white)}
.stat-num{display:flex;align-items:center;gap:8px;font-size:25px;font-weight:700}
.stat-label{font-size:10.5px;font-weight:700;margin-top:6px}
.subscribe-input{left:653px;top:2258px;width:256px;height:35px;border:1px solid #666;font-size:10px;color:#999;padding:0 14px;line-height:33px}
.subscribe-btn{left:917px;top:2258px;width:107px;height:35px;background:var(--blue);color:var(--white);font-size:11px;font-weight:700;text-align:center;line-height:35px}
.foot-head{top:2338px;font-size:13.5px;font-weight:700;color:var(--white);text-transform:uppercase;padding-bottom:6px;border-bottom:2px solid #777}
.foot-text{font-size:10.5px;line-height:15.5px;color:var(--footer-text)}
.foot-list{list-style:none;font-size:11px;color:var(--footer-text);line-height:19px}
.foot-list li::before{content:"›";margin-right:6px}
.contact-row{display:flex;gap:12px;font-size:10.5px;line-height:14px;color:var(--footer-text)}
.social{top:2478px;left:887px;display:flex;gap:10px}
.social span{width:22px;height:22px;border-radius:50%;border:1px solid #888}
.copy{left:0;top:2545px;width:1200px;height:49px;background:var(--blue);color:var(--white);font-size:12px;text-align:center;line-height:49px}
</style>
</head>
<body>

<header class="abs hero">
</header>
<div class="abs hero-photo" role="img" aria-label="Photograph of assorted steel bolts, nuts and washers arranged on a light surface"></div>
<div class="abs brand"><span class="brand-dot"></span><span class="brand-name">KRV Holdfast Group</span></div>
<ul class="abs nav">
  <li>Home</li><li>Products</li><li>Capabilities</li><li>Engineering</li><li>Quality</li><li>About Us</li><li>Contact/Quote Request</li>
</ul>
<h1 class="abs tagline"><span class="l1">Better Fasteners</span><span class="l2">For</span><span class="l3">Better Products</span></h1>

<!-- welcome -->
<h2 class="abs welcome-title">Welcome to <em>Holdfast</em> <i>Group</i></h2>
<p class="abs welcome-lead">KRV Holdfast Group is a leading designer and manufacturer of value added, high quality engineered hardware solutions.</p>
<p class="abs welcome-body">It is a long established fact that a reader will be distracted by the readable content of a page when looking at its layout. The point of using Lorem Ipsum is that it has a more-or-less normal distribution of letters, as opposed to using 'Content here, content here', making it look like readable English.</p>
<div class="abs feature-line"></div>
<div class="abs feature" style="top:818px">
  <span class="feature-icon"><svg width="22" height="22" viewBox="0 0 22 22"><circle cx="11" cy="11" r="7" fill="none" stroke="#fff" stroke-width="2.5"/><circle cx="11" cy="11" r="2.5" fill="#fff"/></svg></span>
  <div><h3>Quality</h3><p>Lorem Ipsum is simply dummy text of the printing and typesetting industry. Lorem Ipsum has been the industry's standard dummy text</p></div>
</div>
<div class="abs feature" style="top:900px">
  <span class="feature-icon"><svg width="22" height="22" viewBox="0 0 22 22"><circle cx="11" cy="11" r="8" fill="none" stroke="#fff" stroke-width="2"/><path d="M7 11l3 3 5-6" fill="none" stroke="#fff" stroke-width="2"/></svg></span>
  <div><h3>Capabilities</h3><p>Lorem Ipsum is simply dummy text of the printing and typesetting industry. Lorem Ipsum has been the industry's standard dummy text</p></div>
</div>
<div class="abs feature" style="top:982px">
  <span class="feature-icon"><svg width="22" height="22" viewBox="0 0 22 22"><path d="M5 11a6 6 0 0 1 12 0z" fill="#fff"/><rect x="4" y="12" width="14" height="2" fill="#fff"/><path d="M7 15h8v4H7z" fill="none" stroke="#fff" stroke-width="1.6"/></svg></span>
  <div><h3>Engineering</h3><p>Lorem Ipsum is simply dummy text of the printing and typesetting industry. Lorem Ipsum has been the industry's standard dummy text</p></div>
</div>
<div class="abs welcome-photo" role="img" aria-label="Photograph of two engineers in hard hats and safety vests inspecting a turbine"></div>

<!-- services -->
<section class="abs services"></section>
<div class="abs services-kicker">View Our</div>
<h2 class="abs services-title">Services</h2>
<div class="abs services-rule"></div>
<p class="abs services-text" style="top:1232px">Lorem ipsum dolor sit amet, consectetur adipiscing elit. Donec dapibus odio vel tellus finibus placerat. In vel purus sed lacus sodales venenatis. Integer et convallis nulla, in fringilla....</p>
<p class="abs services-text" style="top:1286px">lobortis ut et leo. Fusce vehicula nisl sed vulputate convallis. Integer consequat, enim eu tempus vulputate, libero eros lacinia dolor, sit amet pretium enim est eget est. Phasellus.</p>
<div class="abs btn-dark" style="left:147px;top:1356px;width:118px;height:31px">Read More <span>›</span></div>

<div class="abs service-tile" style="left:577px;top:1127px">
  <div class="service-photo" role="img" aria-label="Photograph of brass bolts with lock washers" style="background:linear-gradient(135deg,#8a7a4a,#c8b060 50%,#6f6a5a)"></div>
  <div class="service-label">Lock Washers</div>
</div>
<div class="abs service-tile" style="left:820px;top:1127px">
  <div class="service-photo" role="img" aria-label="Photograph of a pile of assorted metal pins" style="background:linear-gradient(135deg,#3a3530,#8a7e70 50%,#2e2a26)"></div>
  <div class="service-label">Pins</div>
</div>
<div class="abs service-tile" style="left:577px;top:1271px">
  <div class="service-photo" role="img" aria-label="Photograph of assorted stamped metal parts" style="background:linear-gradient(135deg,#c9c9c9,#9a9a9a 50%,#d9d9d9)"></div>
  <div class="service-label">Stampings</div>
</div>
<div class="abs service-tile" style="left:820px;top:1271px">
  <div class="service-photo" role="img" aria-label="Photograph of long threaded rods" style="background:linear-gradient(135deg,#f2f2f2,#6b5e52 50%,#e8e8e8)"></div>
  <div class="service-label">Threaded</div>
</div>

<!-- quote -->
<section class="abs quote"></section>
<div class="abs field" style="left:147px;top:1477px;width:188px">Name / Company Name</div>
<div class="abs field" style="left:344px;top:1477px;width:189px">Email</div>
<div class="abs field" style="left:541px;top:1477px;width:189px">Phone Number</div>
<div class="abs field" style="left:147px;top:1518px;width:188px">Number Of Case</div>
<div class="abs field" style="left:344px;top:1518px;width:189px">Number Of Outgoing Invoice</div>
<div class="abs field" style="left:541px;top:1518px;width:189px">Number Of Incoming Invoice</div>
<div class="abs btn-dark" style="left:147px;top:1561px;width:168px;height:31px">Get A Free Quote <svg width="14" height="8" viewBox="0 0 14 8"><path d="M0 4h12M9 1l3 3-3 3" fill="none" stroke="#fff" stroke-width="1.6"/></svg></div>
<svg class="abs quote-mark" width="56" height="46" viewBox="0 0 56 46"><path d="M0 0h24v26c0 10-6 18-16 20v-8c4-1 7-5 7-10H0zM32 0h24v26c0 10-6 18-16 20v-8c4-1 7-5 7-10H32z" fill="#fff"/></svg>
<div class="abs quote-kicker">Get A Free Quote</div>
<h2 class="abs quote-title">Our Services</h2>

<!-- news -->
<h2 class="abs news-title">Our Recent News</h2>
<div class="abs news-rule"></div>

<article class="abs news-card is-active" style="left:147px;top:1770px">
  <div class="news-photo" role="img" aria-label="Photograph of industrial machinery on a factory floor" style="background:linear-gradient(135deg,#5d7a6a,#a9b3b0 50%,#3f4f58)"><div class="news-date"><b>20</b><small>SEP</small></div></div>
  <div class="news-body"><h4>Nam vel lectus non sapien</h4><div class="news-meta"><span>● Admin</span><span>● 10 Comments</span></div><p>printing and typesetting industry. Lorem Ipsum has been the industry's standard dummy text took a galley of type and scrambled it to make type specimen book.</p></div>
</article>
<article class="abs news-card" style="left:626px;top:1770px">
  <div class="news-photo" role="img" aria-label="Photograph of two machined steel bolts" style="background:linear-gradient(135deg,#b08a66,#d7d4cf 50%,#8a6a50)"><div class="news-date"><b>20</b><small>SEP</small></div></div>
  <div class="news-body"><h4>Nam vel lectus non sapien</h4><div class="news-meta"><span>● Admin</span><span>● 10 Comments</span></div><p>printing and typesetting industry. Lorem Ipsum has been the industry's standard dummy text took a galley of type and scrambled it to make type specimen book.</p></div>
</article>
<article class="abs news-card" style="left:147px;top:1966px">
  <div class="news-photo" role="img" aria-label="Photograph of a bin of fasteners beside production equipment" style="background:linear-gradient(135deg,#4f6a4a,#777 50%,#2f3a30)"><div class="news-date"><b>20</b><small>SEP</small></div></div>
  <div class="news-body"><h4>Nam vel lectus non sapien</h4><div class="news-meta"><span>● Admin</span><span>● 10 Comments</span></div><p>printing and typesetting industry. Lorem Ipsum has been the industry's standard dummy text took a galley of type and scrambled it to make type specimen book.</p></div>
</article>
<article class="abs news-card" style="left:626px;top:1966px">
  <div class="news-photo" role="img" aria-label="Photograph of a machining line in a workshop" style="background:linear-gradient(135deg,#8a8680,#cfcac2 50%,#5a524a)"><div class="news-date"><b>20</b><small>SEP</small></div></div>
  <div class="news-body"><h4>Nam vel lectus non sapien</h4><div class="news-meta"><span>● Admin</span><span>● 10 Comments</span></div><p>printing and typesetting industry. Lorem Ipsum has been the industry's standard dummy text took a galley of type and scrambled it to make type specimen book.</p></div>
</article>

<!-- footer -->
<footer class="abs footer"></footer>
<div class="abs stat" style="left:147px">
  <div class="stat-num"><svg width="24" height="22" viewBox="0 0 24 22"><rect x="1" y="3" width="22" height="18" fill="none" stroke="#2a9fd6" stroke-width="2"/><rect x="1" y="3" width="22" height="5" fill="#2a9fd6"/><path d="M5 12h3M10 12h3M15 12h3M5 16h3M10 16h3M15 16h3" stroke="#2a9fd6" stroke-width="2"/></svg>23</div>
  <div class="stat-label">Offices worldwide</div>
</div>
<div class="abs stat" style="left:283px">
  <div class="stat-num"><svg width="28" height="22" viewBox="0 0 28 22"><circle cx="14" cy="6" r="5" fill="#2a9fd6"/><circle cx="5" cy="8" r="3.5" fill="#2a9fd6"/><circle cx="23" cy="8" r="3.5" fill="#2a9fd6"/><path d="M6 22a8 8 0 0 1 16 0zM0 20a5 5 0 0 1 8-4v4zM28 20a5 5 0 0 0-8-4v4z" fill="#2a9fd6"/></svg>15</div>
  <div class="stat-label">Hardworking people</div>
</div>
<div class="abs stat" style="left:432px">
  <div class="stat-num"><svg width="22" height="22" viewBox="0 0 22 22"><circle cx="11" cy="11" r="10" fill="#2a9fd6"/><path d="M6 6c3 1 4 4 2 6s1 5 3 6M15 4c-1 3 2 4 4 5" fill="none" stroke="#1f1f1f" stroke-width="2"/></svg>20</div>
  <div class="stat-label">Countries covered</div>
</div>
<div class="abs subscribe-input">Your Email Address</div>
<div class="abs subscribe-btn">SUBSCRIBE</div>

<h5 class="abs foot-head" style="left:150px;border-bottom:none">Shortly About Us</h5>
<p class="abs foot-text" style="left:150px;top:2372px;width:190px">Lorem Ipsum is simply dummy text the printing and typesetting industry. Lorem Ipsum has been the industry's text 1500s, when an unknown printer took a galley of type and scrambled it to make not only five centuries, but also the leap including versions of Lorem Ipsum.</p>

<h5 class="abs foot-head" style="left:419px;width:167px">Recent Blog</h5>
<div class="abs" style="left:419px;top:2375px;width:180px">
  <p class="foot-text">Mauris ultricies ante quis neque nec accumsan lorem finibus Lorem</p>
  <p class="foot-text" style="margin:6px 0 10px">◷ &nbsp;March 25,2016</p>
  <p class="foot-text">Mauris ultricies ante quis neque nec accumsan lorem finibus Lorem</p>
  <p class="foot-text" style="margin-top:6px">◷ &nbsp;March 25,2016</p>
</div>

<h5 class="abs foot-head" style="left:674px;width:130px">Information</h5>
<ul class="abs foot-list" style="left:674px;top:2372px">
  <li>Home</li><li>About Us</li><li>Capabilities</li><li>Engineering</li><li>Quality</li><li>About Us</li><li>Contact/Quote Request</li>
</ul>

<h5 class="abs foot-head" style="left:887px;width:167px">Contact Us</h5>
<div class="abs" style="left:887px;top:2372px;width:180px">
  <div class="contact-row"><svg width="10" height="14" viewBox="0 0 10 14"><path d="M5 0a5 5 0 0 1 5 5c0 4-5 9-5 9S0 9 0 5a5 5 0 0 1 5-5z" fill="#bbb"/><circle cx="5" cy="5" r="2" fill="#1f1f1f"/></svg><span>418 Kestrel Mill Road<br>Ashford Vale, IL 60999</span></div>
  <div class="contact-row" style="margin-top:14px"><svg width="12" height="10" viewBox="0 0 12 10"><rect width="12" height="10" fill="#bbb"/><path d="M0 0l6 5 6-5" fill="none" stroke="#1f1f1f" stroke-width="1.2"/></svg><span>sales@holdfastgroup.example</span></div>
  <div class="contact-row" style="margin-top:16px"><svg width="12" height="12" viewBox="0 0 12 12"><path d="M2 0l3 3-1.5 2a7 7 0 0 0 3.5 3.5L9 7l3 3-2 2C5 12 0 7 0 2z" fill="#bbb"/></svg><span>555-014-2652</span></div>
</div>
<div class="abs social"><span></span><span></span><span></span><span></span><span></span></div>

<div class="abs copy">© 2017 holdfastgroup.example . All rights reserved.</div>

</body>
</html>
```